Quartz Pivot Business Card Design

I need a 2-sided business card for my computer engineering consulting company. The card is expected to convey a message of cutting edge forward thinking, and boldnes. I would like the card to be memorable and stand-out on a desk. The card should be bold, modern, clean, and highly professional. I am a big fan of watermarks/shadows and other intersting but restrained uses of the logo. The card can be a shape other than the traditional rectangle. Perhaps a rectangle with rounded edges. All I ask is the card be able to fit into a standard wallet. I will supply two logos, one with a red background, and one with a black background. Please feel free to work with both of these logos.
Updates

Hi all, thank you for your submissions. I will post the original vector file later today. Thank you for your patience.

Regards,

Martin

Target Market(s)

Engineering Buyers, Vice Presidents and Directors

Industry/Entity Type

Computer

Requirements
Must have
• 2 sides

```html
<!DOCTYPE html>
<html lang="en">
<head>
<meta charset="utf-8">
<title>Quartz Pivot Works – Business Card</title>
<link href="https://fonts.googleapis.com/css2?family=Questrial&display=swap" rel="stylesheet">
<style>
  :root {
    --backdrop: #d9dde0;
    --card-white: #ffffff;
    --card-black: #2a2a2a;
    --brand-red: #c8202a;
    --ink: #1e1e1e;
    --muted-grey: #8a8a8a;
    --light-grey: #bfbfbf;
  }
  * { box-sizing: border-box; margin: 0; padding: 0; }
  html, body {
    width: 1200px;
    height: 960px;
    overflow: hidden;
  }
  body {
    background: var(--backdrop);
    font-family: "Questrial", "Century Gothic", sans-serif;
    display: flex;
    flex-direction: column;
    align-items: center;
    justify-content: center;
    gap: 56px;
  }
  .card {
    position: relative;
    width: 700px;
    height: 400px;
    border-radius: 34px;
    box-shadow: 0 6px 18px rgba(0,0,0,0.18);
    overflow: hidden;
  }

  /* ---------- Front ---------- */
  .card-front { background: var(--card-white); color: var(--ink); }
  .front-brand {
    position: absolute;
    top: 58px;
    right: 46px;
    text-align: right;
  }
  .brand-name {
    font-size: 30px;
    color: var(--brand-red);
    letter-spacing: 0.5px;
    white-space: nowrap;
  }
  .brand-tagline {
    font-size: 12.5px;
    color: var(--muted-grey);
    letter-spacing: 2.4px;
    margin-top: 4px;
    white-space: nowrap;
  }
  .name-bar {
    position: absolute;
    left: 0;
    top: 146px;
    width: 14px;
    height: 82px;
    background: var(--brand-red);
  }
  .person {
    position: absolute;
    left: 46px;
    top: 146px;
  }
  .person-name { font-size: 44px; line-height: 1.05; font-weight: 400; }
  .person-role { font-size: 28px; margin-top: 8px; }
  .contact-list {
    position: absolute;
    left: 46px;
    top: 268px;
    list-style: none;
  }
  .contact-item {
    display: flex;
    align-items: center;
    gap: 12px;
    font-size: 20px;
    line-height: 1;
    margin-bottom: 8px;
    white-space: nowrap;
  }
  .contact-icon {
    width: 20px;
    height: 20px;
    background: var(--brand-red);
    color: var(--card-white);
    font-size: 14px;
    display: flex;
    align-items: center;
    justify-content: center;
    border-radius: 2px;
  }

  /* ---------- Back ---------- */
  .card-back {
    background: var(--card-black);
    display: flex;
    align-items: center;
    justify-content: center;
  }
  .back-brand { text-align: center; }
  .back-brand-row {
    display: flex;
    align-items: center;
    justify-content: center;
    gap: 16px;
  }
  .brand-square {
    width: 30px;
    height: 30px;
    background: var(--brand-red);
  }
  .back-brand .brand-name { font-size: 44px; }
  .back-brand .brand-tagline {
    font-size: 17px;
    color: var(--light-grey);
    letter-spacing: 4px;
    margin-top: 8px;
  }
</style>
</head>
<body>

  <section class="card card-front" aria-label="Business card front">
    <div class="front-brand">
      <div class="brand-name">QUARTZ PIVOT WORKS LTD</div>
      <div class="brand-tagline">ENGINEERING BEYOND LIMITS</div>
    </div>

    <div class="name-bar"></div>
    <div class="person">
      <h1 class="person-name">Tom Hadley</h1>
      <p class="person-role">IT Director</p>
    </div>

    <ul class="contact-list">
      <li class="contact-item"><span class="contact-icon">t</span>0161 482 7390 ext 2215</li>
      <li class="contact-item"><span class="contact-icon">e</span>tom.hadley@quartzpivot.com</li>
      <li class="contact-item"><span class="contact-icon">w</span>www.quartzpivot.com</li>
      <li class="contact-item"><span class="contact-icon">a</span>Unit 4, Mill Lane, Westbridge, WB3 7LT</li>
    </ul>
  </section>

  <section class="card card-back" aria-label="Business card back">
    <div class="back-brand">
      <div class="back-brand-row">
        <span class="brand-square"></span>
        <span class="brand-name">QUARTZ PIVOT WORKS LTD</span>
      </div>
      <div class="brand-tagline">ENGINEERING BEYOND LIMITS</div>
    </div>
  </section>

</body>
</html>
```